The (Closed) News Relaying Report

This is a professional and academic report of 35 pages for journalists and teachers. The topic of the report is News Sharing: journalism, social networks and technology. Attached there is an example of the kind of design we are looking for: visual, fresh and modern.

Target Market(s)

Journalists, Journalism Students, Communication Researchers,

Industry/Entity Type

Media

Font styles to use
Sans Serif

Colors
3276b5
33a6d7
886aae
b868aa

Requirements
Must have
• Copyleft images, visual style
Nice to have
• There is an example attached.

```html
<!DOCTYPE html>
<html lang="en">
<head>
<meta charset="utf-8">
<title>The (Closed) News Relaying Report – Page Layouts</title>
<link rel="stylesheet" href="https://fonts.googleapis.com/css2?family=Nunito+Sans:ital,wght@0,400;0,600;0,700;0,800;0,900;1,400&display=swap">
<style>
:root{
  --sky:#4fb0dd;
  --sky-soft:#86c9ea;
  --brand:#33a6d7;
  --deep:#3276b5;
  --violet:#886aae;
  --pink:#b868aa;
  --ink:#1d1d1f;
  --stage:#c9c9c9;
  --row:#e6e6e6;
  --paper:#ffffff;
}
*{margin:0;padding:0;box-sizing:border-box}
html,body{width:1200px;height:2382px;overflow:hidden}
body{background:var(--stage);font-family:"Nunito Sans",sans-serif;color:var(--ink);position:relative}
.abs{position:absolute}
.sheet-label{position:absolute;width:490px;font-size:23px;font-weight:600;text-align:center;letter-spacing:.5px;line-height:30px}
.page{position:absolute;width:490px;height:693px;background:var(--paper);overflow:hidden;box-shadow:0 2px 6px rgba(0,0,0,.15)}
.col-a{left:108px}
.col-b{left:615px}
.row-1{top:870px}
.row-2{top:1583px}
/* cover */
.cover-sky{position:absolute;left:0;top:0;width:490px;height:262px}
.cover-kicker{top:62px;left:0;width:490px;text-align:center;color:#fff;font-size:21px;font-weight:400;letter-spacing:.3px}
.cover-title{top:84px;left:0;width:490px;text-align:center;color:#fff;font-size:40px;font-weight:900;letter-spacing:.4px;line-height:48px}
.cover-sub{top:141px;left:0;width:490px;text-align:center;color:#fff;font-size:17px;line-height:21px}
.cover-art{left:78px;top:200px;width:318px;height:278px;border-radius:16px;background:linear-gradient(135deg,#dff1fb 0%,#9fd6f0 45%,#3276b5 80%,#b868aa 100%)}
.cover-credit{top:536px;left:0;width:490px;text-align:center;font-size:11.5px;line-height:15.5px}
.cover-credit strong{font-weight:800;letter-spacing:.2px}
.cover-year{top:612px;left:0;width:490px;text-align:center;font-size:38px;line-height:50px;font-weight:900;color:var(--brand)}
/* inner */
.rule{position:absolute;left:67px;top:0;width:3px;background:var(--brand)}
.intro-lead{left:86px;top:84px;font-size:27px;line-height:34px;font-weight:600}
.author-name{left:86px;top:117px;font-size:26px;line-height:36px;font-weight:900;color:var(--brand)}
.body-copy{left:66px;top:214px;width:356px;font-size:9.6px;line-height:13.6px;text-align:justify}
.body-copy p{margin-bottom:13px}
.section-title{font-size:27px;line-height:34px;font-weight:900;color:var(--brand);letter-spacing:.4px}
.index-title{left:85px;top:153px}
.intro-title{left:86px;top:116px}
.network-haze{right:0;top:0;width:320px;height:210px;background:radial-gradient(ellipse at 70% 30%,rgba(180,190,200,.28),rgba(255,255,255,0) 70%)}
.index-table{left:64px;top:213px;width:369px;list-style:none}
.index-table li{display:flex;justify-content:space-between;height:18px;line-height:18px;padding:0 17px;margin-bottom:9.1px;font-size:9.3px}
.index-table li:nth-child(odd){background:var(--row)}
.index-table li.major{font-weight:800}
.index-table li span:last-child{font-weight:800}
.index-art{left:204px;top:411px;width:229px;height:282px;border-radius:18px 18px 0 0;background:linear-gradient(160deg,#eaf4fb 0%,#8fb8e0 40%,#3276b5 75%,#e9a57a 100%);z-index:2}
.intro-copy{left:82px;top:158px;width:340px;font-size:7.9px;line-height:11.6px;text-align:justify}
.intro-copy p{margin-bottom:9px}
.wave{position:absolute;left:0;bottom:0;width:490px;height:118px}
.page-foot{position:absolute;left:19px;right:19px;bottom:15px;display:flex;justify-content:space-between;color:#fff;font-size:8.8px;z-index:3}
.page-foot b{font-weight:800}
</style>
</head>
<body>
<div class="sheet-label col-a" style="top:827px">COVER PAGE 1</div>
<div class="sheet-label col-b" style="top:827px">COVER PAGE 2</div>

<section class="page col-a row-1">
  <svg class="cover-sky" viewBox="0 0 490 262" preserveAspectRatio="none">
    <path d="M0 0H490V262C455 255 420 205 375 203C320 201 280 226 200 238C120 248 60 240 0 234Z" fill="var(--sky)"/>
  </svg>
  <div class="abs cover-kicker">THE (CLOSED) NEWS</div>
  <h1 class="abs cover-title">RELAYING REPORT</h1>
  <div class="abs cover-sub">A starting guide for<br>researchers and journalists</div>
  <div class="abs cover-art" role="img" aria-label="Illustration of a person writing with a giant pencil on an open laptop beside a stack of books"></div>
  <div class="abs cover-credit">
    <strong>A REPORT BY ELENA MARÍN SOLER</strong><br>
    <em>Visiting Scholar at the Eastbridge University (Harbor City, USA)<br>with the help of Research Grants 18/19 from the Valdemar University<br>of Sierra Alta (Sierra Alta, Spain)</em>
  </div>
  <div class="abs cover-year">2019</div>
</section>

<section class="page col-b row-1">
  <div class="rule" style="height:182px"></div>
  <div class="abs intro-lead">This is a report by</div>
  <div class="abs author-name">ELENA MARÍN<br>SOLER (PHD),</div>
  <div class="abs body-copy">
    <p>a journalist working at the Valdemar University of Sierra Alta (UVAL, Spain), where she is the Head of the Communication Sciences Department. This project has been supported by a research grant from UVAL to do a research stay as a Visiting Scholar at the Eastbridge University (EU), USA, and the help of professor Daniel Roark at EU.</p>
    <p>Special thanks goes to those who collaborated in the interviews: the journalists at the Global Reporters Forum (GRF), The Capital Ledger, Horizon Media Network, Voces TV, The Open Record Center, The Iberia Brief, Checkpoint and Verifica. In addition, I also want to thank the whole faculty members at the School of Communication at the Eastbridge University (EU-SOC), who always offered their collaboration.</p>
    <p>Special thanks also goes to colleagues and scholars who selflessly dedicated their time to talk and hold meetings. They shed light on many topics reflected in to go through the report in depth. They are Tomás Verde, Nadia Karim, Lucía Ferrer-Banks, Helen Osterby, Ruth Calder, Iker Montes, Paul Whitford, and Grace Tellman.</p>
    <p>The interviews are expressions of personal opinions as journalists and they do not necessarily express the official point of view of the media where they work. Inquiries for further information about this research can be sent to emarin.report@mailbox.test or emarin@uval.edu</p>
  </div>
  <svg class="wave" viewBox="0 0 490 118" preserveAspectRatio="none">
    <path d="M0 40C50 5 100 5 160 30C230 60 290 78 360 58C410 44 455 36 490 38V118H0Z" fill="var(--sky-soft)"/>
    <path d="M0 42C60 18 120 30 180 58C250 88 320 86 390 66C440 52 470 50 490 52V118H0Z" fill="var(--sky)"/>
  </svg>
  <div class="page-foot"><span>THE (CLOSED) NEWS <b>RELAYING REPORT</b></span><span>PAGE - 1</span></div>
</section>

<section class="page col-a row-2">
  <div class="abs network-haze" role="img" aria-label="Faint network of connected dots"></div>
  <div class="rule" style="height:182px"></div>
  <h2 class="abs section-title index-title">INDEX</h2>
  <ul class="abs index-table">
    <li class="major"><span>INTRODUCTION</span><span>4</span></li>
    <li class="major"><span>RESEARCH QUESTIONS</span><span>5</span></li>
    <li><span>1. The Media Landscape</span><span>6</span></li>
    <li><span>2. The Interviews</span><span>11</span></li>
    <li><span>3. The Best Practices</span><span>29</span></li>
    <li><span>4. Conclusions</span><span>31</span></li>
    <li><span>5. References</span><span>33</span></li>
  </ul>
  <div class="abs index-art" role="img" aria-label="Illustration of a hand holding a smartphone surrounded by people, ratings and chat icons"></div>
  <svg class="wave" viewBox="0 0 490 118" preserveAspectRatio="none">
    <path d="M0 40C50 5 100 5 160 30C230 60 290 78 360 58C410 44 455 36 490 38V118H0Z" fill="var(--sky-soft)"/>
    <path d="M0 42C60 18 120 30 180 58C250 88 320 86 390 66C440 52 470 50 490 52V118H0Z" fill="var(--sky)"/>
  </svg>
  <div class="page-foot"><span>THE (CLOSED) NEWS <b>RELAYING REPORT</b></span><span>PAGE - 2</span></div>
</section>

<section class="page col-b row-2">
  <div class="abs network-haze" role="img" aria-label="Faint network of connected dots"></div>
  <div class="rule" style="height:146px"></div>
  <h2 class="abs section-title intro-title">INTRODUCTION</h2>
  <div class="abs intro-copy">
    <p>The job of journalists is not just longer on the internet because it ends later, it is also longer because it starts before. On the Internet, on the one hand, a journalist can have a community even before having a journalistic product. On the other hand, social recommendations, incidental consumption of news and online private messages are giving a broader reach to journalism, as we know it now.</p>
    <p>Because publishing is not the end of the journalistic routine, the whole process now is longer. You cannot fully understand what "news" means for people if you do not understand how and why they are sharing the news on online private platforms. Private messaging networks are adding new challenges to journalists and the media. When we are talking about online private environments, issues such as sources, fact-checking, misinformation, privacy or (fake) news are being redefined, as well as the notions of trust, community, public service and media literacy.</p>
    <p>In 2018 President Ruy Almada was accused of running a whole fake news campaign through ChatLine with hundreds of millions of messages against his opponent. This scandal is just an example of the growing relevance of fact-checking and the need to for media literacy skills among users of private messaging networks.</p>
    <p>Many news sites added a ChatLine sharing option in their news during the last few years (Halvorsen, 2014) and it seems like private channels, such as this one, could become a "major traffic driver for news sites" (Lindqvist, A., Marrow, V., &amp; Pettit, T., 2015: 10). We cannot entirely know what people are doing with news in private messaging networks, but what we can see is what the media and journalists are doing with these platforms. This report is a draft of these actions.</p>
    <p>In news sharing research, a new broad theoretical foundation is needed, with quantitative studies, digital ethnographies or uses and gratifications approaches, and even combining these theories and deriving new ones. We utilize the results of this preliminary research to provide insights so that journalism can be improved, and academic research of journalism can move forward in news sharing research.</p>
    <p>The main goal of this executive report is to help journalists and researchers to get a deeper understanding of the news sharing processes in private messaging apps, channels, and networks. Share it, but not in a private way. Make it as public as you can.</p>
  </div>
  <svg class="wave" viewBox="0 0 490 118" preserveAspectRatio="none">
    <path d="M0 40C50 5 100 5 160 30C230 60 290 78 360 58C410 44 455 36 490 38V118H0Z" fill="var(--sky-soft)"/>
    <path d="M0 42C60 18 120 30 180 58C250 88 320 86 390 66C440 52 470 50 490 52V118H0Z" fill="var(--sky)"/>
  </svg>
  <div class="page-foot"><span>THE (CLOSED) NEWS <b>RELAYING REPORT</b></span><span>PAGE - 3</span></div>
</section>

<div class="sheet-label col-a" style="top:2306px">INNER PAGE 1</div>
<div class="sheet-label col-b" style="top:2306px">INNER PAGE 2</div>
</body>
</html>
```